Kelvar Engineering Business Card Design

We need a new business card for our engineering consultancy, Kelvar Engineering. The card should look sharp and professional.

Kelvar Engineering is mechanical engineering consultancy providing engineering services and testing. We mainly serve the automotive enthusiast (certifying modified vehicles) and trade sectors (product development & certification). The company also provides general mechanical engineering consultancy, and services to the railway industry.

The logo attached should be used.

Location: Adelaide, South Australia

Target Market(s)

Individual Clients, and corporate clients

Industry/Entity Type

Mechanical Engineering

Requirements
Must have
• Front:

Kelvar Engineering Pty Ltd
PO Box 417
Fernhollow, SA 5093

Gavin Trelowarth MBA,BEng(Mech), MIEAust CPEng
gtrelowarth@kelvarengineering.com.au
kelvarengineering.com.au
mobile +61 (0)491 308 574

Back
Modified Vehicle Engineering & Testing
Component Design & Analysis
Individually Constructed Vehicle Engineering
Australian Design Rule (ADR) Compliance Testing
General Mechanical Engineering
Permanent Way Engineering Services
Rail Plant and Equipment Services

Nice to have
• embossing
Should not have
• Photographs or images other than the logo.

```html
<!DOCTYPE html>
<html lang="en">
<head>
<meta charset="utf-8">
<title>Kelvar Engineering – Business Card</title>
<link href="https://fonts.googleapis.com/css2?family=Montserrat:wght@400;500&display=swap" rel="stylesheet">
<style>
  :root {
    --backdrop: #e8e8e9;
    --card: #ffffff;
    --navy: #0d2b4a;
    --blue: #2a8fd0;
    --sky: #5cc6f2;
    --ink: #2d3640;
    --muted: #5b6570;
  }
  html, body {
    margin: 0;
    width: 1200px;
    height: 718px;
    overflow: hidden;
    background: var(--backdrop);
    font-family: "Montserrat", Arial, sans-serif;
  }
  .card {
    position: absolute;
    left: 170px;
    top: 109px;
    width: 860px;
    height: 500px;
    background: var(--card);
    box-shadow: 0 10px 30px rgba(0,0,0,0.12);
    overflow: hidden;
  }
  .card-wave {
    position: absolute;
    inset: 0;
    width: 860px;
    height: 500px;
  }
  .brand {
    position: absolute;
    left: 430px;
    top: 92px;
    width: 300px;
    text-align: center;
  }
  .brand-dot {
    width: 64px;
    height: 64px;
    border-radius: 50%;
    background: var(--blue);
    margin: 0 auto 18px;
  }
  .brand-name {
    font-size: 27px;
    font-weight: 400;
    letter-spacing: 1px;
    color: var(--navy);
    white-space: nowrap;
  }
  .contact {
    position: absolute;
    left: 58px;
    top: 236px;
    color: var(--ink);
  }
  .contact-name {
    font-size: 25px;
    font-weight: 500;
    letter-spacing: 1px;
    color: var(--blue);
    text-transform: uppercase;
    margin: 0;
  }
  .contact-role {
    font-size: 15px;
    color: var(--muted);
    margin: 4px 0 16px;
  }
  .contact-address {
    font-size: 13px;
    line-height: 19px;
    font-style: normal;
    margin-bottom: 14px;
  }
  .contact-list {
    list-style: none;
    margin: 0;
    padding: 0;
    font-size: 12px;
    line-height: 21px;
  }
  .contact-list li {
    display: flex;
    align-items: center;
    gap: 9px;
  }
  .contact-icon {
    width: 13px;
    height: 13px;
    flex: none;
  }
</style>
</head>
<body>
  <div class="card">
    <svg class="card-wave" viewBox="0 0 860 500" aria-hidden="true">
      <defs>
        <linearGradient id="waveFill" x1="0" y1="1" x2="1" y2="0">
          <stop offset="0" stop-color="#1f7fc2"/>
          <stop offset="0.5" stop-color="#5cc6f2"/>
          <stop offset="1" stop-color="#2a8fd0"/>
        </linearGradient>
      </defs>
      <path d="M300 500 C 480 472, 560 330, 860 300 L860 500 Z" fill="url(#waveFill)"/>
      <path d="M275 500 C 470 462, 545 312, 860 284" fill="none" stroke="#0d2b4a" stroke-width="6"/>
      <path d="M340 500 C 520 480, 600 360, 860 330" fill="none" stroke="#ffffff" stroke-opacity="0.35" stroke-width="3"/>
    </svg>

    <div class="brand">
      <div class="brand-dot"></div>
      <div class="brand-name">KELVAR ENGINEERING</div>
    </div>

    <div class="contact">
      <h1 class="contact-name">Gavin Trelowarth</h1>
      <p class="contact-role">Managing Director</p>
      <address class="contact-address">PO Box 417<br>Fernhollow, SA 5093</address>
      <ul class="contact-list">
        <li>
          <svg class="contact-icon" viewBox="0 0 16 16"><path d="M4 1l3 3-2 2c1 2 3 4 5 5l2-2 3 3-2 3C7 15 1 9 1 3z" fill="#2a8fd0"/></svg>
          Ph: +61 (0)8 8317 4402
        </li>
        <li>
          <svg class="contact-icon" viewBox="0 0 16 16"><rect x="2" y="5" width="12" height="8" rx="1" fill="#2a8fd0"/><rect x="4" y="1" width="8" height="5" fill="none" stroke="#2a8fd0" stroke-width="1.5"/></svg>
          Fax: +61 (0)8 8317 4403
        </li>
        <li>
          <svg class="contact-icon" viewBox="0 0 16 16"><rect x="4" y="1" width="8" height="14" rx="1.5" fill="#2a8fd0"/><rect x="5.5" y="3" width="5" height="8" fill="#fff"/></svg>
          Mob: +61 (0)491 308 574
        </li>
        <li>
          <svg class="contact-icon" viewBox="0 0 16 16"><rect x="1" y="3" width="14" height="10" rx="1" fill="#2a8fd0"/><path d="M1.5 4l6.5 5 6.5-5" fill="none" stroke="#fff" stroke-width="1.3"/></svg>
          gtrelowarth@kelvarengineering.com.au
        </li>
        <li>
          <svg class="contact-icon" viewBox="0 0 16 16"><circle cx="8" cy="8" r="7" fill="#2a8fd0"/><path d="M1 8h14M8 1c-3 4-3 10 0 14M8 1c3 4 3 10 0 14" fill="none" stroke="#fff" stroke-width="1"/></svg>
          kelvarengineering.com.au
        </li>
      </ul>
    </div>
  </div>
</body>
</html>
```